VIP Fashion Nightclub Flyer Design

Brass and Velvet is set to be a platform for fashion brands, artists and designers to showcase their talents. In the past, launch parties etc. would have had to be organised by the brand itself. Brass and Velvet aims to provide a direct link with the fashion community.

We need a flyer design for our nightclubs grand opening. We would like to see designs that use mostly black on black. We also would like to create a feeling of luxury and exclusivity. Please see fashion editorials for reference.

See below for flyer text:

Brass & Velvet
X
Gilt Heron

GRAND OPENING
Sydney’s Most Exclusive Event
SATURDAY 12th OF MAY 2012

General 10PM – LATE
VIP 9PM - LATE

Register today for an invite:
www.velvetroomguest.com.au

Live Music and DJ’s

The Larkmere Hotel
87 Callow St
Quenbury

Hi guys, ive added some images like our logo and wax stamps that we use for our personal invitations.

Target Market(s)

Brass and Velvet targets 20-30 year olds in the fashion industry, models, retailers and designers.

Industry/Entity Type

Fashion

Requirements
Must have
• Must be made into 3 sizes:
A1
Chatterpage Cover Art
1000px x 1000px

```html
<!DOCTYPE html>
<html lang="en">
<head>
<meta charset="utf-8">
<title>Brass &amp; Velvet – Grand Opening Flyers</title>
<link href="https://fonts.googleapis.com/css2?family=Questrial&display=swap" rel="stylesheet">
<style>
  :root {
    --sheet: #ffffff;
    --ink: #ffffff;
    --accent: #d81fdc;
    --rule: rgba(255,255,255,0.75);
    --sequin-dark: #141414;
    --sequin-mid: #3a3a3a;
    --sequin-light: #8a8a8a;
    --band: rgba(0,0,0,0.28);
  }
  * { margin: 0; padding: 0; box-sizing: border-box; }
  html, body {
    width: 1200px; height: 843px; overflow: hidden;
    background: var(--sheet);
    font-family: "Questrial", "Century Gothic", sans-serif;
    color: var(--ink);
  }
  .sheet { position: relative; width: 1200px; height: 843px; }

  .flyer { position: absolute; overflow: hidden; }
  .flyer--poster { left: 26px; top: 23px; width: 564px; height: 797px; }
  .flyer--square { left: 608px; top: 24px; width: 566px; height: 567px; }
  .flyer--banner { left: 608px; top: 611px; width: 566px; height: 209px; }

  .sequin-field {
    position: absolute; inset: 0;
    background:
      radial-gradient(ellipse 40% 30% at 20% 10%, rgba(170,170,170,0.55), transparent 70%),
      radial-gradient(ellipse 35% 25% at 85% 20%, rgba(140,140,140,0.45), transparent 70%),
      radial-gradient(ellipse 30% 25% at 15% 90%, rgba(120,120,120,0.4), transparent 70%),
      radial-gradient(ellipse 40% 30% at 90% 85%, rgba(110,110,110,0.35), transparent 70%),
      radial-gradient(circle at 50% 50%, var(--sequin-mid), var(--sequin-dark) 80%);
  }

  .band {
    position: absolute; left: 0; right: 0;
    background: var(--band);
    border-top: 1px solid var(--rule);
    border-bottom: 1px solid var(--rule);
  }

  .line {
    position: absolute; left: 0; right: 0;
    text-align: center; white-space: nowrap;
    transform: translateY(-50%);
    line-height: 1;
  }
  .brand { font-size: 80px; letter-spacing: 1px; }
  .collab { font-size: 27px; letter-spacing: -0.5px; }
  .headline { font-size: 41px; color: var(--accent); letter-spacing: -1px; }
  .detail { font-size: 20px; }
  .feature { font-size: 29px; color: var(--accent); }

  /* banner sizes */
  .flyer--banner .logo-block { position: absolute; left: 0; top: 0; width: 326px; height: 209px; }
  .flyer--banner .info-block { position: absolute; left: 317px; top: 0; width: 215px; height: 209px; }
  .flyer--banner .brand { font-size: 62px; }
  .flyer--banner .collab { font-size: 21px; }
  .flyer--banner .headline { font-size: 20px; letter-spacing: -0.5px; }
  .flyer--banner .detail { font-size: 11px; }
  .flyer--banner .feature { font-size: 15px; }
  .rule { position: absolute; left: 0; right: 0; height: 1px; background: var(--rule); }
</style>
</head>
<body>
<main class="sheet">

  <!-- A1 poster -->
  <section class="flyer flyer--poster">
    <div class="sequin-field" role="img" aria-label="Black and silver sequin texture background"></div>
    <div class="band" style="top:318px;height:106px;"></div>
    <div class="line brand" style="top:129px;">BRASS &amp;</div>
    <div class="line brand" style="top:201px;">VELVET</div>
    <div class="line collab" style="top:258px;">X GILT HERON</div>
    <div class="line headline" style="top:350px;">GRAND OPENING</div>
    <div class="line detail" style="top:382px;">Sydney’s Most Exclusive Event</div>
    <div class="line detail" style="top:404px;">SATURDAY 12th OF MAY 2012</div>
    <div class="line detail" style="top:471px;">General 10PM – LATE</div>
    <div class="line detail" style="top:494px;">VIP 9PM - LATE</div>
    <div class="line detail" style="top:539px;">Register today for an invite:</div>
    <div class="line detail" style="top:563px;">www.velvetroomguest.com.au</div>
    <div class="line feature" style="top:604px;">Live Music and DJ’s</div>
    <div class="line detail" style="top:652px;">The Larkmere Hotel</div>
    <div class="line detail" style="top:675px;">87 Callow St</div>
    <div class="line detail" style="top:697px;">Quenbury</div>
  </section>

  <!-- Cover art -->
  <section class="flyer flyer--square">
    <div class="sequin-field" role="img" aria-label="Black and silver sequin texture background"></div>
    <div class="band" style="top:249px;height:100px;"></div>
    <div class="line brand" style="top:83px;">BRASS &amp;</div>
    <div class="line brand" style="top:156px;">VELVET</div>
    <div class="line collab" style="top:210px;">X GILT HERON</div>
    <div class="line headline" style="top:279px;">GRAND OPENING</div>
    <div class="line detail" style="top:308px;">Sydney’s Most Exclusive Event</div>
    <div class="line detail" style="top:328px;">SATURDAY 12th OF MAY 2012</div>
    <div class="line detail" style="top:381px;">General 10PM – LATE - VIP 9PM - LATE</div>
    <div class="line detail" style="top:416px;">Register today for an invite:</div>
    <div class="line detail" style="top:436px;">www.velvetroomguest.com.au</div>
    <div class="line feature" style="top:476px;">Live Music and DJ’s</div>
    <div class="line detail" style="top:513px;">The Larkmere Hotel 87 Callow St Quenbury</div>
  </section>

  <!-- Web banner -->
  <section class="flyer flyer--banner">
    <div class="sequin-field" role="img" aria-label="Black and silver sequin texture background"></div>
    <div class="logo-block">
      <div class="line brand" style="top:66px;">BRASS &amp;</div>
      <div class="line brand" style="top:122px;">VELVET</div>
      <div class="line collab" style="top:163px;">X GILT HERON</div>
    </div>
    <div class="info-block">
      <div class="rule" style="top:33px;"></div>
      <div class="line headline" style="top:49px;">GRAND OPENING</div>
      <div class="line detail" style="top:66px;">Sydney’s Most Exclusive Event</div>
      <div class="line detail" style="top:77px;">SATURDAY 12th OF MAY 2012</div>
      <div class="rule" style="top:87px;"></div>
      <div class="line detail" style="top:106px;">General 10PM – LATE - VIP 9PM - LATE</div>
      <div class="line detail" style="top:125px;">Register today for an invite:</div>
      <div class="line detail" style="top:137px;">www.velvetroomguest.com.au</div>
      <div class="line feature" style="top:160px;">Live Music and DJ’s</div>
      <div class="line detail" style="top:180px;">The Larkmere Hotel 87 Callow St Quenbury</div>
    </div>
  </section>

</main>
</body>
</html>
```